Magician | Speaker looks for an innovative business card design

I'm a magician and public speaker offering artistic and modern magical experiences.
I'm based in Brussels (Belgium.) I love magic performed up-close, creating a space of intimacy, even when I'm on stage.
The final design should communicate professionalism, elegance, artistry, and a friendly kind personality

I would like to see designs based either on my photos and/or the way I sign my name Remy Vok (see attached files for more info.)
Additional photos and more info about what I offer can be seen at www.remy-vok.net

My current business card design is also attached. I like the fact that the reverse of my current design includes quotes from master magicians about magic, changing the way my participants see the art of magic.

Note: I would like a double-sided card design. However, I need white space on the reverse to be able to write things on for my performances.

Details to include on the card:
Artist name: Remy Vok
Offer: magician + (public) speaker or magic + (public) speaking (the + sign can be replaced by another character, like a bullet or a pipe)
Phone: +32 471 265 903
Email: book@remy-vok.net
(optional) Website: www.remy-vok.net or remy-vok.net

Target Market(s)

Corporate, organisations, companies as well as individuals

Industry/Entity Type

Artists

Colors

Designer to choose colors to be used in the design.

Requirements
Nice to have
• A side with a mirror could be nice

```html
<!DOCTYPE html>
<html lang="en">
<head>
<meta charset="utf-8">
<title>Remy Vok — Business Card</title>
<link rel="stylesheet" href="https://fonts.googleapis.com/css2?family=Roboto:wght@400;500&display=swap">
<style>
  :root {
    --page-bg: #2a2422;
    --card-black: #0b0b0b;
    --gold: #d9a520;
    --gold-light: #f0c84a;
    --text-light: #e8e8e8;
    --paper-white: #ffffff;
    --photo-brick-a: #8a5a3c;
    --photo-brick-b: #3a2a22;
    --photo-red-a: #6e1a1e;
    --photo-red-b: #1e0c0d;
    --stripe: #050505;
  }
  * { margin: 0; padding: 0; box-sizing: border-box; }
  html, body { width: 1200px; height: 780px; overflow: hidden; }
  body {
    background: var(--page-bg);
    font-family: "Roboto", Arial, sans-serif;
    display: flex;
    align-items: center;
    justify-content: center;
    gap: 40px;
  }
  .card {
    position: relative;
    width: 540px;
    height: 320px;
    overflow: hidden;
    box-shadow: 0 14px 30px rgba(0,0,0,.45);
  }
  .card-front { background: var(--card-black); }

  .photo {
    position: absolute;
    overflow: hidden;
  }
  .photo-left {
    left: 0; top: 0; width: 150px; height: 320px;
    background: linear-gradient(160deg, var(--photo-brick-a) 0%, #5e3d2b 45%, var(--photo-brick-b) 100%);
  }
  .photo-right {
    right: 0; top: 0; width: 150px; height: 200px;
    background: linear-gradient(200deg, var(--photo-red-a) 0%, #3d1215 55%, var(--photo-red-b) 100%);
  }
  .photo-right::after {
    content: "";
    position: absolute; inset: 0;
    background: linear-gradient(to bottom, rgba(11,11,11,0) 60%, var(--card-black) 100%);
  }
  .photo-left::after {
    content: "";
    position: absolute; inset: 0;
    background: linear-gradient(to right, rgba(11,11,11,0) 70%, var(--card-black) 100%);
  }
  .stripe {
    position: absolute;
    top: 0; bottom: 0;
    width: 7px;
    background: var(--stripe);
    z-index: 1;
  }

  .brand {
    position: absolute;
    left: 170px; top: 110px;
    width: 230px;
    text-align: center;
    color: var(--gold);
    font-weight: 500;
    font-size: 44px;
    letter-spacing: 1px;
  }
  .offer {
    position: absolute;
    left: 0; right: 0; top: 228px;
    text-align: center;
    color: var(--gold);
    font-weight: 500;
    font-size: 14px;
  }
  .contact {
    position: absolute;
    left: 0; right: 0; top: 254px;
    text-align: center;
    color: var(--text-light);
    font-size: 12px;
    letter-spacing: .2px;
  }
  .contact .dot { margin: 0 7px; }

  .card-back { background: var(--paper-white); }
  .back-band {
    position: absolute;
    left: 0; top: 0; bottom: 0;
    width: 130px;
    background: var(--card-black);
    display: flex;
    align-items: center;
    justify-content: center;
  }
  .back-brand {
    color: var(--paper-white);
    font-weight: 500;
    font-size: 20px;
    transform: rotate(-90deg);
    white-space: nowrap;
  }
</style>
</head>
<body>
  <section class="card card-front" aria-label="Card front">
    <div class="photo photo-left" role="img" aria-label="Photo of the magician laughing among soap bubbles in front of a brick wall">
      <span class="stripe" style="left:24px"></span>
      <span class="stripe" style="left:52px"></span>
      <span class="stripe" style="left:80px"></span>
      <span class="stripe" style="left:108px"></span>
    </div>
    <div class="photo photo-right" role="img" aria-label="Photo of the magician holding up playing cards against a red backdrop">
      <span class="stripe" style="left:30px"></span>
      <span class="stripe" style="left:62px"></span>
      <span class="stripe" style="left:94px"></span>
    </div>
    <div class="brand">Remy Vok</div>
    <p class="offer">Magician + (public) speaker</p>
    <p class="contact">+32 471 265 903<span class="dot">•</span>book@remy-vok.net<span class="dot">•</span>www.remy-vok.net</p>
  </section>

  <section class="card card-back" aria-label="Card back">
    <div class="back-band">
      <span class="back-brand">Remy Vok</span>
    </div>
  </section>
</body>
</html>
```